Commercial Construction Company

We need a business card design based on our current logo. We are a commercial general contractor based in Southern California that specializes in bank remodels. We would like to see designs that incorporate dark blue. The final design should portray an image of professionalism and quality.

If possible, I would like to add metallic foil to the design. Thank you

```html
<!DOCTYPE html>
<html lang="en">
<head>
<meta charset="utf-8">
<title>Northgate Builders – Business Card</title>
<link rel="stylesheet" href="https://fonts.googleapis.com/css2?family=Lato:wght@400;700&display=swap">
<style>
  :root {
    --page-bg: #dcdcdc;
    --card-bg: #23272e;
    --card-bg-deep: #1c2026;
    --brand-blue: #12508f;
    --brand-blue-bright: #1d5fae;
    --swoosh-grey: #a9a9a6;
    --text-light: #f4f1e6;
    --divider: #8a8d92;
  }
  * { box-sizing: border-box; margin: 0; padding: 0; }
  html, body { width: 1200px; height: 787px; overflow: hidden; }
  body {
    background: var(--page-bg);
    font-family: "Lato", sans-serif;
    display: flex;
    align-items: center;
    justify-content: center;
    gap: 40px;
  }
  .card {
    position: relative;
    width: 520px;
    height: 310px;
    border-radius: 14px;
    overflow: hidden;
    background: linear-gradient(160deg, var(--card-bg) 0%, var(--card-bg-deep) 100%);
    box-shadow: 0 6px 18px rgba(0,0,0,0.25);
  }
  .card__waves { position: absolute; inset: 0; width: 100%; height: 100%; }
  .brand {
    position: absolute;
    display: flex;
    align-items: center;
    gap: 12px;
    color: var(--text-light);
    font-weight: 700;
    line-height: 1.05;
  }
  .brand__dot {
    width: 26px; height: 26px; border-radius: 50%;
    background: var(--brand-blue-bright);
    flex: none;
  }
  .brand__name { font-size: 34px; }
  .card--back .brand { left: 158px; top: 80px; }
  .card--front .brand { left: 34px; top: 74px; }
  .card--front .brand__name { font-size: 28px; }
  .divider {
    position: absolute;
    left: 254px; top: 92px;
    width: 1px; height: 130px;
    background: var(--divider);
    transform: rotate(14deg);
    transform-origin: top left;
  }
  .contact {
    position: absolute;
    left: 276px; top: 80px;
    color: var(--text-light);
    font-size: 13px;
    line-height: 1.45;
  }
  .contact__name {
    color: var(--brand-blue-bright);
    font-weight: 700;
    font-size: 15px;
    text-transform: uppercase;
    letter-spacing: 0.5px;
  }
  .contact__role { margin-bottom: 6px; }
  .contact__list { list-style: none; margin-top: 8px; }
  .contact__list li { display: flex; align-items: center; gap: 8px; }
  .contact__list svg { width: 11px; height: 11px; flex: none; fill: var(--brand-blue-bright); }
</style>
</head>
<body>

  <section class="card card--back" aria-label="Business card back">
    <svg class="card__waves" viewBox="0 0 520 310" preserveAspectRatio="none" aria-hidden="true">
      <path d="M0,150 C80,240 280,288 520,296 L520,310 L0,310 Z" fill="var(--swoosh-grey)"/>
      <path d="M0,162 C90,250 290,296 520,304 L520,310 L0,310 Z" fill="var(--card-bg-deep)"/>
      <path d="M0,158 C30,220 90,280 170,310 L0,310 Z" fill="var(--brand-blue)"/>
    </svg>
    <div class="brand">
      <span class="brand__dot"></span>
      <div class="brand__name">Northgate<br>Builders</div>
    </div>
  </section>

  <section class="card card--front" aria-label="Business card front">
    <svg class="card__waves" viewBox="0 0 520 310" preserveAspectRatio="none" aria-hidden="true">
      <path d="M0,150 C80,240 280,290 520,298 L520,310 L0,310 Z" fill="var(--swoosh-grey)"/>
      <path d="M0,162 C90,252 290,298 520,305 L520,310 L0,310 Z" fill="var(--card-bg-deep)"/>
      <path d="M0,158 C30,220 90,280 170,310 L0,310 Z" fill="var(--brand-blue)"/>
    </svg>
    <div class="brand">
      <span class="brand__dot"></span>
      <div class="brand__name">Northgate<br>Builders</div>
    </div>
    <span class="divider"></span>
    <div class="contact">
      <div class="contact__name">Owen Carver</div>
      <div class="contact__role">President</div>
      <div>1280 Linden Avenue, Crestmoor</div>
      <div>CA 9, United States</div>
      <ul class="contact__list">
        <li><svg viewBox="0 0 12 12"><path d="M2.5 0.5 L4.5 0.5 L5.2 3.2 L3.8 4.3 C4.4 5.8 6.2 7.6 7.7 8.2 L8.8 6.8 L11.5 7.5 L11.5 9.5 C11.5 10.6 10.6 11.5 9.5 11.5 C4.5 11.5 0.5 7.5 0.5 2.5 C0.5 1.4 1.4 0.5 2.5 0.5 Z"/></svg>000-000-000-000</li>
        <li><svg viewBox="0 0 12 12"><path d="M3 0 H9 A1 1 0 0 1 10 1 V11 A1 1 0 0 1 9 12 H3 A1 1 0 0 1 2 11 V1 A1 1 0 0 1 3 0 Z M3.5 1.5 V9.5 H8.5 V1.5 Z"/></svg>000-000-000-000</li>
        <li><svg viewBox="0 0 12 12"><path d="M0 2 H12 V10 H0 Z M0.8 2.6 L6 6.6 L11.2 2.6 L11.2 3.6 L6 7.6 L0.8 3.6 Z" fill-rule="evenodd"/></svg>info@websitename.com</li>
        <li><svg viewBox="0 0 12 12"><path d="M6 0 A6 6 0 1 0 6 12 A6 6 0 1 0 6 0 Z M6 1.2 C7 2.4 7.5 4 7.6 5.4 H4.4 C4.5 4 5 2.4 6 1.2 Z M4.4 6.6 H7.6 C7.5 8 7 9.6 6 10.8 C5 9.6 4.5 8 4.4 6.6 Z M1.3 5.4 C1.5 3.6 2.7 2.1 4.3 1.5 C3.6 2.6 3.2 4 3.2 5.4 Z M1.3 6.6 H3.2 C3.2 8 3.6 9.4 4.3 10.5 C2.7 9.9 1.5 8.4 1.3 6.6 Z M8.8 5.4 C8.8 4 8.4 2.6 7.7 1.5 C9.3 2.1 10.5 3.6 10.7 5.4 Z M8.8 6.6 H10.7 C10.5 8.4 9.3 9.9 7.7 10.5 C8.4 9.4 8.8 8 8.8 6.6 Z"/></svg>www.websitename.com</li>
      </ul>
    </div>
  </section>

</body>
</html>
```